Business Card/ Car Magnet/ Polo Shirt/ Envelope/ Letterhead Design Project
Birchmont Property Valuations, LLC.
Business Card/ Car Magnet/ Polo Shirt/ Envelope/ Letterhead Design Project - Real Estate
Creative Brief
Professional
Gus Talbottine
State Certified Residential Real Estate Appraiser
14 Coldmeadow Ln Maplecrest, NJ 08199
gtalbottine@birchmontvaluations.example
valuemarkhq.example
NJ- 57RC00913400 PA- RL284615 DE- X2-0000317
Please be creative...
gust1983 gust1983
Hello, Just wanted to clarify some of the common questions asked so far. The colors to incorporate would be blue, green and white (unless of course you would like to incorporate other colors for creativity) . please feel free to incorporate them any way you see fit. The polo shirts will be done on white, black and royal blue shirts. Please be as creative as you like. Thanks you for your efforts and for participating! Please reply back with any further questions. Thanks! BPV

```html
<!DOCTYPE html>
<html lang="en">
<head>
<meta charset="utf-8">
<title>Birchmont Property Valuations — Stationery</title>
<link href="https://fonts.googleapis.com/css2?family=Cinzel:wght@600&family=Open+Sans:wght@400;600&display=swap" rel="stylesheet">
<style>
:root{
  --bg:#e6e8ea;
  --paper:#ffffff;
  --blue:#1b5a9a;
  --navy:#0d3d6e;
  --green:#3a8a3c;
  --lime:#6ab04c;
  --ink:#3a3f44;
  --muted:#8a9096;
  --faint:#eef2f5;
}
*{box-sizing:border-box;margin:0;padding:0}
html,body{width:1200px;height:713px;overflow:hidden;background:var(--bg);font-family:"Open Sans",sans-serif;color:var(--ink)}
.canvas{position:relative;width:1200px;height:713px}
.sheet{position:absolute;background:var(--paper);box-shadow:0 2px 8px rgba(0,0,0,.18);overflow:hidden}
.band{height:10px;background:linear-gradient(90deg,var(--navy),var(--blue) 60%,var(--green))}
.band-thin{height:4px;background:var(--lime)}
.logo{display:flex;align-items:center;gap:6px;font-family:"Cinzel",serif;font-weight:600;color:var(--navy)}
.logo .dot{border-radius:50%;background:var(--green);flex:none}
.logo-stack{text-align:center;font-family:"Cinzel",serif;font-weight:600;color:var(--navy)}
.watermark{position:absolute;border-radius:50%;background:var(--faint)}
.card{width:270px;height:150px}
.card .name{font-size:13px;font-weight:600}
.card .title{font-size:8px;color:var(--muted)}
.card .info{font-size:7.5px;line-height:1.5}
.card--blue{background:linear-gradient(160deg,var(--blue),var(--navy));color:#fff}
.card--green{background:linear-gradient(160deg,var(--lime),var(--green));color:#fff}
.card--blue .logo-stack,.card--green .logo-stack{color:#fff}
.letter{left:320px;top:20px;width:380px;height:673px}
.letter .body{padding:14px 34px;font-size:8.5px;line-height:1.7}
.letter .foot{position:absolute;left:0;right:0;bottom:0;padding:8px 24px;font-size:7px;color:var(--muted);border-top:3px solid var(--lime);display:flex;justify-content:space-between;gap:8px;white-space:nowrap}
.sign{margin-top:18px}
.sign .line{width:120px;height:22px;border-bottom:1px solid var(--ink);margin:6px 0 4px}
</style>
</head>
<body>
<div class="canvas">

  <div class="sheet card" style="left:30px;top:20px">
    <div class="band"></div>
    <div style="padding:12px 16px">
      <div class="name">Gus Talbottine</div>
      <div class="title">State Certified Residential Real Estate Appraiser</div>
      <div class="info" style="margin-top:10px">14 Coldmeadow Ln Maplecrest, NJ 08199<br>(555) 014-2290<br>gtalbottine@birchmontvaluations.example<br>valuemarkhq.example</div>
      <div class="info" style="color:var(--muted)">NJ- 57RC00913400 &nbsp;PA- RL284615 &nbsp;DE- X2-0000317</div>
    </div>
  </div>

  <div class="sheet card" style="left:30px;top:190px">
    <div class="watermark" style="right:-30px;top:20px;width:120px;height:120px"></div>
    <div style="position:relative;padding-top:42px" class="logo-stack">
      <div style="font-size:30px">BPV</div>
      <div style="font-size:8px;color:var(--blue)">Birchmont Property Valuations, LLC.</div>
    </div>
    <div class="band" style="position:absolute;bottom:0;left:0;right:0"></div>
  </div>

  <div class="sheet card card--green" style="left:30px;top:360px">
    <div style="padding-top:44px" class="logo-stack">
      <div style="font-size:30px">BPV</div>
      <div style="font-size:8px">Birchmont Property Valuations, LLC.</div>
    </div>
  </div>

  <div class="sheet card card--blue" style="left:30px;top:530px">
    <div style="padding-top:44px" class="logo-stack">
      <div style="font-size:30px">BPV</div>
      <div style="font-size:8px">Birchmont Property Valuations, LLC.</div>
    </div>
    <div class="band-thin" style="position:absolute;bottom:0;left:0;right:0"></div>
  </div>

  <div class="sheet letter">
    <div class="band"></div>
    <div class="band-thin"></div>
    <div class="watermark" style="right:-60px;top:260px;width:260px;height:260px"></div>
    <div class="logo-stack" style="position:relative;padding-top:22px">
      <div style="font-size:36px">BPV</div>
      <div style="font-size:9px;color:var(--blue)">Birchmont Property Valuations, LLC.</div>
    </div>
    <div class="body" style="position:relative">
      <p style="font-size:11px;margin:10px 0 8px">Hello,</p>
      <p>Thank you for choosing our firm for your residential appraisal needs. Our certified team delivers accurate, timely and well documented valuations for purchase, refinance and estate planning. We combine local market knowledge with careful inspection to give you a report you can trust. Please review the enclosed details and contact our office with any questions about your property.</p>
      <p style="margin-top:8px">We look forward to working with you on your next assignment.</p>
      <div class="sign">Regards,<div class="line"></div>Gus Talbottine</div>
    </div>
    <div class="foot"><span>14 Coldmeadow Ln Maplecrest, NJ 08199</span><span>gtalbottine@birchmontvaluations.example</span></div>
  </div>

  <div class="sheet" style="left:730px;top:20px;width:200px;height:250px">
    <div class="band"></div>
    <div class="logo" style="padding:14px 14px 0;font-size:18px"><span class="dot" style="width:10px;height:10px"></span>BPV</div>
    <div style="padding:40px 14px 0;font-size:16px;font-weight:600;color:var(--navy)">Fax Sheet</div>
    <div style="margin:10px 14px;border-top:1px solid var(--lime)"></div>
  </div>

  <div class="sheet" style="left:730px;top:300px;width:440px;height:210px">
    <div class="band"></div>
    <div class="watermark" style="right:-40px;top:40px;width:200px;height:200px"></div>
    <div style="position:relative;padding:16px 20px">
      <div class="logo" style="font-size:22px"><span class="dot" style="width:12px;height:12px"></span>BPV</div>
      <div style="font-size:7.5px;color:var(--blue);margin-top:2px">Birchmont Property Valuations, LLC.</div>
      <div style="font-size:7.5px;color:var(--muted);margin-top:4px">14 Coldmeadow Ln Maplecrest, NJ 08199</div>
    </div>
    <div class="band-thin" style="position:absolute;bottom:0;left:0;right:0"></div>
  </div>

  <div class="sheet" style="left:730px;top:540px;width:440px;height:150px">
    <div class="band"></div>
    <div style="padding:18px 20px">
      <div class="logo" style="font-size:22px"><span class="dot" style="width:12px;height:12px"></span>BPV</div>
      <div style="font-size:7.5px;color:var(--muted);margin-top:6px">14 Coldmeadow Ln Maplecrest, NJ 08199 &nbsp;·&nbsp; (555) 014-2290</div>
    </div>
    <div class="band-thin" style="position:absolute;bottom:0;left:0;right:0"></div>
  </div>

</div>
</body>
</html>
```